Real Estate Development Company Web Developer

Hi, I am looking for a website developer to create a website for our new real estate development company. you need to design a website with motion graphics that can be run on any device.
We're looking for sample websites like:
https://brackenholm.ca/ or https://www.tarnwellco.ca/
- The website shall include 6 pages with 1 page hidden.
- The website needs to have 2 versions - English and Chinese
- for your mock-up design, you can use copyright free imagery (we are based in Vancouver, and our projects are townhouses/condos, etc)
Please show examples of professional websites you have done & a mock-up website design for our company. We will shortlist in the next several days and get started straight away. The wording for text content will be detailed in a separate document for each page after we decide the designer.

```html
<!DOCTYPE html>
<html lang="en">
<head>
<meta charset="utf-8">
<title>Harbourline Properties</title>
<link href="https://fonts.googleapis.com/css2?family=Poppins:wght@500;600;700&family=Lato:wght@400;700&family=Roboto:wght@400;500&display=swap" rel="stylesheet">
<style>
:root{
  --blue:#1565a9;
  --brown:#a14d1f;
  --navy:#061428;
  --ink:#1b1b1b;
  --text:#333;
  --soft:#eef0f3;
  --white:#fff;
}
*{margin:0;padding:0;box-sizing:border-box}
html,body{width:1200px;height:3223px;overflow:hidden}
body{position:relative;background:var(--white);font-family:"Lato",sans-serif;color:var(--text)}
.abs{position:absolute}
/* header */
.site-header{position:absolute;left:0;top:0;width:1200px;height:82px;background:var(--white)}
.brand{position:absolute;left:113px;top:26px;display:flex;align-items:center;gap:8px;font-family:"Poppins",sans-serif;font-weight:700;font-size:22px;color:var(--blue);letter-spacing:.5px}
.brand-mark{width:16px;height:16px;background:var(--blue)}
.nav a{position:absolute;top:29px;font-family:"Roboto",sans-serif;font-size:15px;color:#333;text-decoration:none}
.nav a.active{color:var(--blue);font-weight:500}
.lang{position:absolute;left:822px;top:27px;width:30px;height:20px;background:#1d3f8f;border:2px solid #c8102e}
.lang-caret{position:absolute;left:864px;top:35px;border:5px solid transparent;border-top:6px solid #222}
.btn{position:absolute;display:flex;align-items:center;justify-content:space-between;border-radius:30px;color:var(--white);font-family:"Lato",sans-serif;font-weight:700;font-size:16px;padding:0 6px 0 19px}
.btn .dot{width:38px;height:38px;border-radius:50%;background:var(--white);display:flex;align-items:center;justify-content:center}
.btn-insider{left:907px;top:12px;width:182px;height:52px;background:var(--brown);justify-content:center;padding:0;font-size:15px}
/* hero */
.hero{position:absolute;left:0;top:82px;width:1200px;height:610px;background:linear-gradient(180deg,#a7b6c2 0%,#c9cfd2 45%,#7f9a5b 75%,#5f7f3b 100%)}
.hero-building{position:absolute;left:590px;top:30px;width:440px;height:440px;background:linear-gradient(180deg,#e9e9e6,#c9c9c4);border-radius:160px 10px 0 0}
.hero-eyebrow{position:absolute;left:111px;top:270px;font-family:"Poppins",sans-serif;font-weight:600;font-size:30px;color:var(--white)}
.hero-title{position:absolute;left:110px;top:318px;font-family:"Poppins",sans-serif;font-weight:700;font-size:48px;color:var(--white)}
.hero-text{position:absolute;left:111px;top:390px;width:430px;font-size:15.5px;line-height:26px;color:var(--white)}
.btn-start{left:111px;top:457px;width:169px;height:50px;background:var(--blue)}
.slider-dots{position:absolute;left:1147px;top:350px}
.slider-dots span{display:block;width:12px;height:12px;border-radius:50%;background:var(--white);margin-bottom:8px}
/* section heading */
.section-title{position:absolute;left:0;width:1200px;text-align:center;font-family:"Poppins",sans-serif;font-weight:700;font-size:35px;color:var(--ink)}
.section-title span{border-left:5px solid var(--blue);padding-left:10px}
/* services */
.service-card{position:absolute;top:861px;width:268px;height:303px;background:var(--white);box-shadow:0 4px 18px rgba(0,0,0,.1);text-align:center}
.service-card svg.curve{position:absolute;left:0;top:0}
.service-num{position:absolute;right:28px;top:14px;font-family:"Poppins",sans-serif;font-weight:700;font-size:34px}
.service-icon{position:absolute;left:104px;top:28px}
.service-name{position:absolute;left:0;top:114px;width:100%;font-family:"Poppins",sans-serif;font-weight:600;font-size:15px;color:var(--ink)}
.service-text{position:absolute;left:22px;top:142px;width:224px;font-size:15px;line-height:26px}
.service-go{position:absolute;left:114px;top:231px;width:40px;height:40px;border-radius:50%;background:var(--white);box-shadow:0 2px 10px rgba(0,0,0,.18);display:flex;align-items:center;justify-content:center}
.btn-learn{left:514px;top:1209px;width:170px;height:50px;background:var(--blue)}
/* about */
.about{position:absolute;left:0;top:1345px;width:1200px;height:665px;background:var(--soft)}
.about-text{position:absolute;top:123px;font-size:15.5px;line-height:25.7px;color:#333}
.btn-about{left:631px;top:252px;width:170px;height:50px;background:var(--brown)}
.photo{position:absolute}
.about-frame{position:absolute;left:656px;top:337px;width:401px;height:276px;border:2px solid var(--brown)}
/* projects */
.project{position:absolute;width:314px;height:225px}
.project-caption{position:absolute;left:31px;bottom:30px;font-family:"Poppins",sans-serif;font-weight:600;font-size:15px;color:var(--white)}
.project-plus{position:absolute;right:34px;bottom:20px}
/* footer */
.footer{position:absolute;left:0;top:2723px;width:1200px;height:451px;background:var(--navy);color:var(--white)}
.news-title{position:absolute;left:108px;top:40px;font-family:"Poppins",sans-serif;font-weight:700;font-size:25px}
.field{position:absolute;top:34px;width:262px;height:45px;border-radius:12px;background:var(--white);color:#444;font-size:15px;padding:13px 20px}
.btn-sub{position:absolute;left:957px;top:33px;width:134px;height:47px;border-radius:24px;background:var(--blue);font-family:"Poppins",sans-serif;font-weight:700;font-size:15px;display:flex;align-items:center;justify-content:center}
.rule{position:absolute;left:110px;top:109px;width:979px;height:1px;background:#3a4656}
.foot-brand{position:absolute;left:111px;top:167px;display:flex;align-items:center;gap:8px;font-family:"Lato",sans-serif;font-weight:700;font-size:22px;color:var(--blue)}
.foot-about{position:absolute;left:111px;top:228px;width:230px;font-size:15.5px;line-height:26px}
.foot-head{position:absolute;font-family:"Poppins",sans-serif;font-weight:600;font-size:15px}
.social{position:absolute;top:333px;width:35px;height:35px;border:1.5px solid var(--white);border-radius:50%}
.links{position:absolute;top:190px;list-style:none;font-size:15.5px}
.links li{height:39px}
.links li::before{content:"»";margin-right:16px}
.contact-ico{position:absolute;left:868px;width:34px;height:34px;border-radius:50%;background:#152338;display:flex;align-items:center;justify-content:center}
.contact-label{position:absolute;left:915px;font-size:13px;font-weight:700}
.contact-val{position:absolute;left:915px;font-size:15.5px;line-height:23px}
.bottom-bar{position:absolute;left:0;top:3174px;width:1200px;height:49px;background:var(--blue);color:var(--white);text-align:center;font-size:14px;line-height:49px}
</style>
</head>
<body>

<header class="site-header">
  <div class="brand"><span class="brand-mark"></span>HARBOURLINE</div>
  <nav class="nav">
    <a class="active" style="left:340px">HOME</a>
    <a style="left:407px">ABOUT US</a>
    <a style="left:502px">OUR SERVICES</a>
    <a style="left:628px">PROJECT</a>
    <a style="left:717px">CONTACT</a>
  </nav>
  <div class="lang" role="img" aria-label="Language selector flag"></div>
  <div class="lang-caret"></div>
  <div class="btn btn-insider">BECOME AN INSIDER</div>
</header>

<section class="hero" role="img" aria-label="Photo of a white curved condominium tower with a green lawn">
  <div class="hero-building"></div>
  <div class="hero-eyebrow">WELCOME TO</div>
  <div class="hero-title">HARBOURLINE</div>
  <p class="hero-text">Lorem ipsum dolor sit amet consectetur adipiscing eli sed do eiusmod tempor incididunt ute labore et dolore magnaited.</p>
  <div class="btn btn-start">GET STARTED<span class="dot"><svg width="16" height="16" viewBox="0 0 16 16"><circle cx="8" cy="8" r="7" fill="var(--blue)"/><path d="M5 8h6M8.5 5.5 11 8l-2.5 2.5" stroke="#fff" stroke-width="1.8" fill="none"/></svg></span></div>
  <div class="slider-dots"><span></span><span></span><span></span><span></span></div>
</section>

<h2 class="section-title" style="top:768px"><span>OUR SERVICES</span></h2>

<article class="service-card" style="left:158px">
  <svg class="curve" width="268" height="303"><path d="M3 150 C3 60 60 4 150 0" stroke="var(--blue)" stroke-width="7" fill="none"/><path d="M265 160 C262 250 210 300 120 303" stroke="var(--blue)" stroke-width="7" fill="none"/></svg>
  <div class="service-num" style="color:var(--blue)">01</div>
  <svg class="service-icon" width="62" height="74"><rect x="4" y="8" width="22" height="66" fill="#3a4a5e"/><rect x="26" y="24" width="32" height="50" fill="var(--blue)"/><g fill="#fff"><rect x="10" y="18" width="4" height="4"/><rect x="17" y="18" width="4" height="4"/><rect x="10" y="30" width="4" height="4"/><rect x="17" y="30" width="4" height="4"/><rect x="33" y="34" width="5" height="5"/><rect x="45" y="34" width="5" height="5"/><rect x="33" y="48" width="5" height="5"/><rect x="45" y="48" width="5" height="5"/></g></svg>
  <div class="service-name">LOREM IPSUM DOLOR</div>
  <p class="service-text">Lorem ipsum dolor sit amet consectetur adipiscing elit sed do eius modadmit tempor.</p>
  <div class="service-go"><svg width="14" height="14"><path d="M2 7h9M7 3l4 4-4 4" stroke="var(--blue)" stroke-width="2.2" fill="none"/></svg></div>
</article>

<article class="service-card" style="left:465px">
  <svg class="curve" width="268" height="303"><path d="M3 150 C3 60 60 4 150 0" stroke="var(--brown)" stroke-width="7" fill="none"/><path d="M265 160 C262 250 210 300 120 303" stroke="var(--brown)" stroke-width="7" fill="none"/></svg>
  <div class="service-num" style="color:var(--brown)">02</div>
  <svg class="service-icon" width="76" height="74"><path d="M20 18 33 6 46 18v20H20z" fill="var(--brown)"/><path d="M2 52h20l12 6 28-12c6-2 10 4 4 8L38 70H2z" fill="var(--blue)"/></svg>
  <div class="service-name">LOREM IPSUM DOLOR</div>
  <p class="service-text">Lorem ipsum dolor sit amet consectetur adipiscing elit sed do eius modadmit tempor.</p>
  <div class="service-go"><svg width="14" height="14"><path d="M2 7h9M7 3l4 4-4 4" stroke="var(--brown)" stroke-width="2.2" fill="none"/></svg></div>
</article>

<article class="service-card" style="left:773px">
  <svg class="curve" width="268" height="303"><path d="M3 150 C3 60 60 4 150 0" stroke="var(--blue)" stroke-width="7" fill="none"/><path d="M265 160 C262 250 210 300 120 303" stroke="var(--blue)" stroke-width="7" fill="none"/></svg>
  <div class="service-num" style="color:var(--blue)">03</div>
  <svg class="service-icon" width="68" height="74"><rect x="16" y="8" width="32" height="56" fill="#3a4a5e"/><g fill="#fff"><rect x="22" y="16" width="5" height="5"/><rect x="30" y="16" width="5" height="5"/><rect x="38" y="16" width="5" height="5"/><rect x="22" y="28" width="5" height="5"/><rect x="30" y="28" width="5" height="5"/><rect x="38" y="28" width="5" height="5"/></g><circle cx="10" cy="56" r="8" fill="var(--blue)"/><circle cx="56" cy="56" r="8" fill="var(--blue)"/><rect x="2" y="64" width="64" height="5" fill="var(--blue)"/></svg>
  <div class="service-name">LOREM IPSUM DOLOR</div>
  <p class="service-text">Lorem ipsum dolor sit amet consectetur adipiscing elit sed do eius modadmit tempor.</p>
  <div class="service-go"><svg width="14" height="14"><path d="M2 7h9M7 3l4 4-4 4" stroke="var(--blue)" stroke-width="2.2" fill="none"/></svg></div>
</article>

<div class="btn btn-learn">LEARN MORE<span class="dot"><svg width="16" height="16"><circle cx="8" cy="8" r="7" fill="var(--blue)"/><path d="M5 8h6M8.5 5.5 11 8l-2.5 2.5" stroke="#fff" stroke-width="1.8" fill="none"/></svg></span></div>

<section class="about">
  <h2 class="section-title" style="top:42px"><span>ABOUT US</span></h2>
  <p class="about-text" style="left:124px;width:462px">Lorem ipsum dolor sit amet, consectetur adipiscing elit, sed eiusmod veniam,quised notrud exercitation ullamcot labori nisi aliquip exedet commodo consequat. Duis aute irure dolor reprehenderit voluptatet velit esse cillum dolore fugiat nulla pariatur. Excepteur sint occaecat cupidatat noin proident culpa qui officia deserunt mollit anim ied est laborum Excepteur occaecat consequat reprehender voluptate velit incididunt nulla aute labore dolore magnat aliqua enim minim.</p>
  <p class="about-text" style="left:631px;width:425px">Lorem ipsum dolor sit amet, consectetur adipiscing elit, sed do eiusmod tempor incididunt Duis aute labore et dolore magnat aliqua enim minim veniam, quised notrud exercitation ullamco labori nisi ut aliquip exed commodo consequat. Duis aute irure officia deserunt mollit laborum Excepteur occaecat commodo</p>
  <div class="btn btn-about">LEARN MORE<span class="dot"><svg width="16" height="16"><circle cx="8" cy="8" r="7" fill="var(--brown)"/><path d="M5 8h6M8.5 5.5 11 8l-2.5 2.5" stroke="#fff" stroke-width="1.8" fill="none"/></svg></span></div>
  <div class="about-frame"></div>
  <div class="photo" style="left:124px;top:319px;width:450px;height:248px;background:linear-gradient(160deg,#c9dcec 0%,#eeeae4 45%,#8fa96a 100%)" role="img" aria-label="Photo of a white modern townhouse block with trees"></div>
  <div class="photo" style="left:539px;top:358px;width:498px;height:234px;background:linear-gradient(120deg,#6a4a3a 0%,#b7c9dc 40%,#1f4a70 75%,#c27a45 100%)" role="img" aria-label="Photo of modern brick and blue condominium buildings"></div>
</section>

<h2 class="section-title" style="top:2085px"><span>OUR PROJECTS</span></h2>

<div class="project" style="left:113px;top:2172px;background:linear-gradient(180deg,#3a7bd0,#8a5a44 55%,#4f7a3a)" role="img" aria-label="Photo of a brick apartment complex"></div>
<div class="project" style="left:443px;top:2172px;background:linear-gradient(180deg,#b8c7d6,#5d6673 50%,#55704a)" role="img" aria-label="Photo of a grey two-storey family house"></div>
<div class="project" style="left:773px;top:2172px;background:linear-gradient(180deg,#d7e3ec,#5f7892 45%,#6c9a3f)" role="img" aria-label="Photo of a blue craftsman house with a garden"></div>
<div class="project" style="left:113px;top:2412px;background:linear-gradient(180deg,#c4d6e2,#dcdcd8 50%,#6f8458)" role="img" aria-label="Photo of white modern townhouses"></div>
<div class="project" style="left:443px;top:2412px;background:linear-gradient(180deg,#5f7aa8,#8d7a6a 55%,#3f3a34)" role="img" aria-label="Photo of a large suburban house at dusk">
  <div class="project-caption">LOREM IPSUM DOLOR SIT</div>
  <svg class="project-plus" width="34" height="34"><circle cx="17" cy="17" r="15" stroke="#fff" stroke-width="1.6" fill="none"/><path d="M17 9v16M9 17h16" stroke="#fff" stroke-width="1.6"/></svg>
</div>
<div class="project" style="left:773px;top:2412px;background:linear-gradient(180deg,#9fbcd8,#d9c2a0 50%,#6a7f48)" role="img" aria-label="Photo of a modern mid-rise condo at sunset"></div>

<footer class="footer">
  <div class="news-title">JOIN OUR NEWSLETTER</div>
  <div class="field" style="left:415px">Enter Your Name:</div>
  <div class="field" style="left:685px">Enter Your Email:</div>
  <div class="btn-sub">SUBSCRIBE</div>
  <div class="rule"></div>

  <div class="foot-brand"><span class="brand-mark"></span>HARBOURLINE</div>
  <p class="foot-about">Lorem ipsum dolor consectetur adipiscing elit sed do eiusmod.</p>
  <div class="foot-head" style="left:111px;top:302px">FOLLOW US</div>
  <div class="social" style="left:110px"></div>
  <div class="social" style="left:152px"></div>
  <div class="social" style="left:195px"></div>
  <div class="social" style="left:237px"></div>

  <div class="foot-head" style="left:418px;top:150px">QUICKLINKS</div>
  <ul class="links" style="left:418px;top:192px"><li>Home</li><li>About us</li><li>Our services</li><li>Project</li><li>Contact</li></ul>
  <div class="foot-head" style="left:664px;top:150px">OTHERLINKS</div>
  <ul class="links" style="left:664px;top:194px"><li>FAQ</li><li>Services</li><li>Privacy Policy</li><li>Returns Policy</li><li>Term of use</li></ul>

  <div class="foot-head" style="left:868px;top:150px">CONTACT US</div>
  <div class="contact-ico" style="top:195px"><svg width="14" height="14" viewBox="0 0 14 14"><path d="M3 1l2.5 3-1.5 1.5c1 2 2.5 3.5 4.5 4.5L10 8.5l3 2.5-1.5 2C7 13 1 7 1 2.5z" fill="#fff"/></svg></div>
  <div class="contact-label" style="top:192px">Phone Number :</div>
  <div class="contact-val" style="top:210px">+ 1888 888 8888</div>
  <div class="contact-ico" style="top:260px"><svg width="15" height="12"><rect x="1" y="1" width="13" height="10" rx="1" stroke="#fff" stroke-width="1.5" fill="none"/><path d="M1 2l6.5 5L14 2" stroke="#fff" stroke-width="1.5" fill="none"/></svg></div>
  <div class="contact-label" style="top:255px">Email:</div>
  <div class="contact-val" style="top:273px">info@harbourlineprops.com</div>
  <div class="contact-ico" style="top:328px"><svg width="12" height="16"><path d="M6 15C2 10 1 8 1 6a5 5 0 0 1 10 0c0 2-1 4-5 9z" fill="#fff"/><circle cx="6" cy="6" r="2" fill="#152338"/></svg></div>
  <div class="contact-label" style="top:323px">Address:</div>
  <div class="contact-val" style="top:341px">12, Lorem ipsum dolor sit<br>consectetur ids adipiscing</div>
</footer>

<div class="bottom-bar">© 2022 Harbourline Properties all rights reserved.</div>

</body>
</html>
```